Tour Guide in Israel business card

I am a tour guide in Israel (the holy land). Prior to it I have over 20 years high-tech business. My main (but not only) focus is working with business people that come to Israel and want to get a tour (usually short from few hours to 2 days). During my guiding I incorporate a lot of my know how of the Israeli business culture. I like to have a business card that I can present to anyone that is looking for a tour guide, but that business people will understand the additional value I can provide them during my tour.

Target Market(s)

Business visitors and tourist to Israel

Industry/Entity Type

Tourism

Contact Information for Business Card

Rory Talbeck
email: rory@talbeck-mail.net
Mobile: +972-52-7164059

Colors

Designer to choose colors to be used in the design.

Requirements
Must have
• Tour Guide
Nice to have
• I don't know how but it should project my understanding in business not just the tourist side of my knowledge.

```html
<!DOCTYPE html>
<html lang="en">
<head>
<meta charset="utf-8">
<title>Rory Talbeck – Tour Guide Business Card</title>
<link rel="stylesheet" href="https://fonts.googleapis.com/css2?family=Quicksand:wght@700&family=Lato:wght@300;400&family=EB+Garamond:ital@1&display=swap">
<style>
  :root {
    --paper: #e9e6dc;
    --navy-light: #1f3d6b;
    --navy: #163259;
    --navy-dark: #0c1e3b;
    --emblem-blue: #4ea8dc;
    --white: #ffffff;
    --caption: #111111;
    --photo-marina-a: #6f8fa6;
    --photo-marina-b: #c9b89a;
    --photo-sea-a: #d8d2c2;
    --photo-sea-b: #34587e;
    --photo-road-a: #a8a18f;
    --photo-road-b: #5d6266;
    --photo-city-a: #7fa9d8;
    --photo-city-b: #c6a67a;
    --photo-station-a: #8fa3ae;
    --photo-station-b: #3f5b63;
    --photo-beach-a: #6aa2d6;
    --photo-beach-b: #dcc59a;
    --photo-mountain-a: #8f8779;
    --photo-mountain-b: #c9b58e;
  }
  html, body {
    margin: 0;
    width: 1200px;
    height: 1200px;
    overflow: hidden;
    background: var(--paper);
  }
  .sheet {
    position: relative;
    width: 1200px;
    height: 1200px;
  }
  .card {
    position: absolute;
    top: 170px;
    width: 420px;
    height: 720px;
    box-shadow: 0 6px 18px rgba(0,0,0,0.25);
  }
  .card--front { left: 120px; }
  .card--back { left: 660px; }
  .card svg { display: block; width: 420px; height: 720px; }
  .card__title {
    font-family: 'Quicksand', sans-serif;
    font-weight: 700;
    fill: var(--white);
  }
  .card__name {
    font-family: 'Lato', sans-serif;
    font-weight: 300;
    fill: var(--white);
  }
  .card__role {
    font-family: 'Lato', sans-serif;
    font-weight: 300;
    fill: var(--white);
  }
  .card__contact {
    font-family: 'Lato', sans-serif;
    font-weight: 300;
    fill: var(--white);
  }
  .caption {
    position: absolute;
    top: 940px;
    width: 420px;
    text-align: center;
    font-family: 'EB Garamond', serif;
    font-style: italic;
    font-size: 40px;
    color: var(--caption);
  }
  .caption--front { left: 120px; }
  .caption--back { left: 660px; }
</style>
</head>
<body>
<div class="sheet">

  <div class="card card--front">
    <svg viewBox="0 0 420 720" xmlns="http://www.w3.org/2000/svg">
      <defs>
        <linearGradient id="navyFront" x1="0" y1="0" x2="1" y2="1">
          <stop offset="0" stop-color="var(--navy-light)"/>
          <stop offset="0.55" stop-color="var(--navy)"/>
          <stop offset="1" stop-color="var(--navy-dark)"/>
        </linearGradient>
        <linearGradient id="marina" x1="0" y1="0" x2="0" y2="1">
          <stop offset="0" stop-color="var(--photo-marina-b)"/>
          <stop offset="1" stop-color="var(--photo-marina-a)"/>
        </linearGradient>
        <linearGradient id="sea" x1="0" y1="0" x2="0" y2="1">
          <stop offset="0" stop-color="var(--photo-sea-a)"/>
          <stop offset="0.45" stop-color="var(--photo-sea-a)"/>
          <stop offset="0.55" stop-color="var(--photo-sea-b)"/>
          <stop offset="1" stop-color="var(--photo-sea-b)"/>
        </linearGradient>
        <linearGradient id="road" x1="0" y1="0" x2="0" y2="1">
          <stop offset="0" stop-color="var(--photo-road-a)"/>
          <stop offset="1" stop-color="var(--photo-road-b)"/>
        </linearGradient>
        <linearGradient id="city" x1="0" y1="0" x2="0" y2="1">
          <stop offset="0" stop-color="var(--photo-city-a)"/>
          <stop offset="1" stop-color="var(--photo-city-b)"/>
        </linearGradient>
        <linearGradient id="station" x1="0" y1="0" x2="0" y2="1">
          <stop offset="0" stop-color="var(--photo-station-a)"/>
          <stop offset="1" stop-color="var(--photo-station-b)"/>
        </linearGradient>
        <linearGradient id="beach" x1="0" y1="0" x2="0" y2="1">
          <stop offset="0" stop-color="var(--photo-beach-a)"/>
          <stop offset="0.4" stop-color="var(--photo-beach-a)"/>
          <stop offset="0.6" stop-color="var(--photo-beach-b)"/>
          <stop offset="1" stop-color="var(--photo-beach-b)"/>
        </linearGradient>
      </defs>

      <rect class="card__background" width="420" height="720" fill="url(#navyFront)"/>

      <g class="photo-strips photo-strips--top">
        <polygon points="22,0 138,0 112,290 0,300 0,40" fill="url(#marina)" role="img" aria-label="Photo of a marina with yachts and palm trees"/>
        <polygon points="152,0 268,0 246,320 126,330" fill="url(#sea)" role="img" aria-label="Photo of seaside hotels above blue water"/>
        <polygon points="282,0 404,0 384,350 260,362" fill="url(#road)" role="img" aria-label="Photo of a highway running through the city"/>
      </g>

      <g class="title">
        <text class="card__title" x="60" y="470" font-size="68">TOUR</text>
        <text class="card__title" x="30" y="550" font-size="68">GUIDE</text>
      </g>

      <rect class="emblem-placeholder" x="272" y="436" width="116" height="130" rx="4" fill="var(--emblem-blue)" fill-opacity="0.35" role="img" aria-label="Outlined blue emblem beside the title"/>

      <g class="photo-strips photo-strips--bottom">
        <polygon points="56,620 170,602 160,720 40,720" fill="url(#city)" role="img" aria-label="Photo of a city skyline with high-rise towers"/>
        <polygon points="184,600 300,582 292,720 172,720" fill="url(#station)" role="img" aria-label="Photo of a train station entrance"/>
        <polygon points="314,580 420,564 420,720 306,720" fill="url(#beach)" role="img" aria-label="Photo of a sandy beach beside an old town"/>
      </g>
    </svg>
  </div>

  <div class="card card--back">
    <svg viewBox="0 0 420 720" xmlns="http://www.w3.org/2000/svg">
      <defs>
        <linearGradient id="navyBack" x1="0" y1="0" x2="1" y2="1">
          <stop offset="0" stop-color="var(--navy-light)"/>
          <stop offset="0.55" stop-color="var(--navy)"/>
          <stop offset="1" stop-color="var(--navy-dark)"/>
        </linearGradient>
        <linearGradient id="mountains" x1="0" y1="0" x2="0" y2="1">
          <stop offset="0" stop-color="var(--photo-mountain-a)"/>
          <stop offset="1" stop-color="var(--photo-mountain-b)"/>
        </linearGradient>
        <linearGradient id="harbour" x1="0" y1="0" x2="1" y2="1">
          <stop offset="0" stop-color="#2f6b8e"/>
          <stop offset="0.6" stop-color="#5a8fa8"/>
          <stop offset="1" stop-color="#b9ab8c"/>
        </linearGradient>
      </defs>

      <rect class="card__background" width="420" height="720" fill="url(#navyBack)"/>

      <rect class="photo photo--mountains" x="0" y="0" width="420" height="96" fill="url(#mountains)" role="img" aria-label="Photo of desert mountains above a coastal town"/>

      <g class="identity" text-anchor="end">
        <text class="card__name" x="396" y="170" font-size="60">Rory</text>
        <text class="card__name" x="396" y="232" font-size="60">Talbeck</text>
        <text class="card__role" x="396" y="272" font-size="26">professional guide</text>
      </g>

      <rect class="photo photo--harbour" x="0" y="300" width="420" height="300" fill="url(#harbour)" role="img" aria-label="Photo of a harbour with moored boats, palm trees and a hotel"/>

      <g class="contact">
        <g class="icon icon--mail">
          <rect x="24" y="628" width="26" height="22" rx="4" fill="var(--white)"/>
          <polyline points="28,634 37,642 46,634" fill="none" stroke="var(--navy)" stroke-width="2.5"/>
        </g>
        <text class="card__contact" x="60" y="648" font-size="25">rory@talbeck-mail.net</text>
        <g class="icon icon--phone">
          <rect x="29" y="666" width="15" height="24" rx="3" fill="none" stroke="var(--white)" stroke-width="2.5"/>
          <line x1="34" y1="685" x2="39" y2="685" stroke="var(--white)" stroke-width="2"/>
        </g>
        <text class="card__contact" x="60" y="688" font-size="25">+972-52-7164059</text>
      </g>
    </svg>
  </div>

  <div class="caption caption--front">front</div>
  <div class="caption caption--back">back</div>

</div>
</body>
</html>
```